DovetailLeaf.com

Updated Website Structure for DovetailLea.com
1. Home Page

(Add social media links in footer or sidebar)
Suggested addition:

Stay Connected
Follow Dovetail Lea for daily encouragement, calming tools, and community stories.

[Facebook Icon] [Instagram Icon] [YouTube Icon]
@DovetailLeaOfficial

2. How It Works

(No major change — keep focused on process and trust building)

3. Ebook Store

(Add social links at the bottom of the page)

Want more free content?
Follow us on social media for sneak peeks, affirmations, and updates on new releases!

[Facebook] [Instagram] [YouTube]

4. Certification Page

(Optional social proof addition)

Connect with Certified Dovetail Leas
Join our online community and see real stories of growth and courage.

Follow us on social media to see how others are supporting each other:

5. Membership Tiers

(Keep page simple, but can include icons in footer)

6. About Me

Suggested addition:

Let’s Stay Connected
I love hearing from others walking this path.

Facebook: @DovetailLeaOfficial

Instagram: @DovetailLeaOfficial

YouTube: Dovetail Lea Channel

7. Disclosure Page

(Keep links in footer only for professional feel.)

8. Global Footer (Site-wide)

Every page should include a calming footer with:

Navigation links (Home | About Me | How It Works | Ebook Store | Certification | Membership | Disclosure)

Social media icons

Copyright info

Example footer text:

🌿 Walking with fear, choosing courage, calming the nervous system together.

© 2025 DovetailLea.com | All rights reserved

```html
<!DOCTYPE html>
<html lang="en">
<head>
<meta charset="UTF-8">
<title>Dovetail Lea — Home</title>
<link rel="stylesheet" href="https://fonts.googleapis.com/css2?family=Lato:wght@400&family=Poppins:wght@600;700&display=swap">
<style>
  :root {
    --page-bg: #faf8f9;
    --hero-dark: #2e0f2e;
    --hero-mid: #4c2752;
    --hero-light: #877099;
    --card: #86729a;
    --badge: #e9c4df;
    --badge-ink: #2b1330;
    --white: #ffffff;
    --nav-line: rgba(255,255,255,0.12);
    --button: #86729a;
    --toggle: #5b4366;
    --caption: #111111;
  }
  * { margin: 0; padding: 0; box-sizing: border-box; }
  html, body { width: 1200px; height: 1200px; overflow: hidden; }
  body { background: var(--page-bg); position: relative; font-family: "Lato", sans-serif; }

  .site {
    position: absolute; left: 37px; top: 153px; width: 1127px; height: 771px;
    background: linear-gradient(125deg, var(--hero-dark) 0%, #3c1740 20%, var(--hero-mid) 45%, #6b4f79 75%, var(--hero-light) 100%);
    overflow: hidden;
  }
  .nav {
    height: 42px; display: flex; align-items: center; padding-left: 15px;
    border-bottom: 1px solid var(--nav-line);
    background: linear-gradient(90deg, rgba(40,15,40,0.5), rgba(120,95,130,0.35));
  }
  .nav-close { width: 10px; height: 10px; margin-right: 24px; }
  .nav-links { display: flex; gap: 23px; list-style: none; }
  .nav-link { display: flex; align-items: center; gap: 8px; color: var(--white); font-size: 13px; letter-spacing: 0.1px; }
  .nav-link svg { width: 13px; height: 12px; fill: var(--white); }
  .theme-toggle {
    position: absolute; right: 14px; top: 15px; width: 44px; height: 21px;
    border-radius: 11px; background: var(--toggle);
  }
  .theme-toggle-knob {
    position: absolute; right: 3px; top: 3px; width: 15px; height: 15px; border-radius: 50%;
    background: var(--white);
  }
  .theme-toggle-knob svg { width: 15px; height: 15px; }

  .hero-card {
    position: absolute; left: 378px; top: 125px; width: 373px; height: 322px;
    background: var(--card); border-radius: 19px;
    display: flex; align-items: center; justify-content: center;
  }
  .brand-badge {
    width: 230px; height: 230px; border-radius: 50%; background: var(--badge);
    display: flex; align-items: center; justify-content: center; margin-top: -24px;
  }
  .brand-name { font-family: "Poppins", sans-serif; font-weight: 600; font-size: 26px; color: var(--badge-ink); }

  .hero-title {
    position: absolute; left: 0; right: 0; top: 472px; text-align: center;
    font-family: "Poppins", sans-serif; font-weight: 700; font-size: 38px; color: var(--white);
  }
  .hero-tagline {
    position: absolute; left: 270px; width: 590px; top: 546px; text-align: center;
    font-size: 15px; line-height: 22px; color: var(--white);
  }
  .hero-button {
    position: absolute; left: 508px; top: 615px; width: 112px; height: 40px;
    border-radius: 20px; background: var(--button); color: var(--white);
    font-family: "Poppins", sans-serif; font-weight: 600; font-size: 12px;
    display: flex; align-items: center; justify-content: center;
  }

  .preview-note { position: absolute; left: 418px; top: 1102px; color: var(--caption); }
  .preview-label { font-size: 16px; }
  .preview-url { font-size: 24px; margin-top: 4px; }
</style>
</head>
<body>
  <div class="site">
    <nav class="nav">
      <svg class="nav-close" viewBox="0 0 10 10"><path d="M1 1L9 9M9 1L1 9" stroke="#fff" stroke-width="1.8"/></svg>
      <ul class="nav-links">
        <li class="nav-link"><svg viewBox="0 0 13 12"><path d="M6.5 0L13 6h-2v6H8V8H5v4H2V6H0z"/></svg>Home</li>
        <li class="nav-link"><svg viewBox="0 0 13 12"><circle cx="4" cy="4" r="3"/><circle cx="9.5" cy="8.5" r="2.5"/><circle cx="4" cy="4" r="1" fill="#5a3a60"/><circle cx="9.5" cy="8.5" r="0.9" fill="#5a3a60"/></svg>How It Works</li>
        <li class="nav-link"><svg viewBox="0 0 13 12"><rect x="2" y="0" width="9" height="12" rx="1.5"/><rect x="4" y="2.5" width="5" height="1" fill="#5a3a60"/></svg>Ebooks</li>
        <li class="nav-link"><svg viewBox="0 0 13 12"><circle cx="6.5" cy="4.5" r="4"/><circle cx="6.5" cy="4.5" r="1.8" fill="#5a3a60"/><path d="M4 8l-1 4 3.5-1.5L10 12 9 8z"/></svg>Certification</li>
        <li class="nav-link"><svg viewBox="0 0 13 12"><circle cx="6.5" cy="3" r="2.3"/><circle cx="2.3" cy="4" r="1.6"/><circle cx="10.7" cy="4" r="1.6"/><path d="M3 11c0-3 1.5-5 3.5-5s3.5 2 3.5 5z"/><path d="M0 10c0-2 1-3.5 2.3-3.5 1 0 1.5 1 1.5 1L3 10zM13 10c0-2-1-3.5-2.3-3.5-1 0-1.5 1-1.5 1L10 10z"/></svg>Membership</li>
        <li class="nav-link"><svg viewBox="0 0 13 12"><circle cx="6.5" cy="3" r="3"/><path d="M1 12c0-4 2.5-5.5 5.5-5.5S12 8 12 12z"/></svg>About</li>
        <li class="nav-link"><svg viewBox="0 0 13 12"><path d="M2.5 0h5.5l3 3v9h-8.5z"/><rect x="4.5" y="6" width="4" height="1" fill="#5a3a60"/><rect x="4.5" y="8" width="4" height="1" fill="#5a3a60"/></svg>Disclosure</li>
      </ul>
      <div class="theme-toggle">
        <div class="theme-toggle-knob"><svg viewBox="0 0 15 15"><path d="M8.5 4a3.6 3.6 0 1 0 2.6 5.8A3 3 0 0 1 8.5 4z" fill="#2b1330"/></svg></div>
      </div>
    </nav>

    <div class="hero-card">
      <div class="brand-badge" role="img" aria-label="Dovetail Leas brand badge">
        <span class="brand-name">Dovetail Leas</span>
      </div>
    </div>

    <h1 class="hero-title">Welcome to Dovetail Lea</h1>
    <p class="hero-tagline">Walking with fear. Choosing courage. Your space for calm, community, and courage through anxiety.</p>
    <div class="hero-button">Get Started</div>
  </div>

  <div class="preview-note">
    <p class="preview-label">Preview your website:</p>
    <p class="preview-url">https://dovetaillea.sitepreview.app/</p>
  </div>
</body>
</html>
```